Motorplume is a mobile and web application, that helps consumers find an auto lease deal.

The process:

1) Create a free account:
a) email
b) password
c) first name
d) last name
e) zipcode
f) phone number ( optional )

-or-

sign in through Chatterloom

-or-

SKIP

Is it OK for dealership to contact customer YES or NO ( check the following )

Would you like to receive news, announcements and daily deals? ( check box)

( privacy policy )

Or Login

2) vehicle(s) currently owned/leased
a) Make
b) Model
c) Year

-SKIP-

3) search by monthly payments or make/model
A. Monthly payments
a. down payment
b. monthly payment min
c. monthly payment max
d. miles
f. years
g. credit score ( optional )

B. By Make and Model
a. model
b. trim
c. miles
d. years
e. down payment
f. credit score ( optional )

4. results
a. list of cars with image that match criteria (need sorting options)
b. detailed lease description of matching vehicle,
c. below show top 3 results of comparable vehicles.

4A. Selected car(s)
a. feature details
(i) performance
(ii) exterior
(iii) interior
(iv) safety
(v) accessories
4B, car locations
i) dealership location with trailvista atlas for a visual.

Target Market(s)

People looking to lease a vehicle

Logo Text

A better way to Lease

Colors

Designer to choose colors to be used in the design.

Requirements
Must have
• Create account
• 4. results
• a. list of cars with image that match criteria (need sorting options)
• b. detailed lease description of matching vehicle,
• c. below show top 3 results of comparable vehicles.
Nice to have
• i) dealership location with trailvista atlas for a visual.

```html
<!DOCTYPE html>
<html lang="en">
<head>
<meta charset="utf-8">
<title>Motorplume – Welcome</title>
<link rel="stylesheet" href="https://fonts.googleapis.com/css2?family=Nunito+Sans:wght@400;600;700;800&display=swap">
<style>
  :root {
    --bg-deep: #1e2b38;
    --bg-mid: #25384b;
    --hero-top: #3e5a78;
    --hero-mid: #33506d;
    --body-light: #8ea6bd;
    --body-mid: #5f7c98;
    --shade: #16212c;
    --white: #ffffff;
    --line: rgba(255,255,255,0.85);
    --accent: #1b74c9;
    --muted: #e4ebf2;
  }
  * { box-sizing: border-box; margin: 0; padding: 0; }
  html, body { width: 675px; height: 1200px; overflow: hidden; }
  body {
    background: var(--bg-deep);
    font-family: "Nunito Sans", sans-serif;
    color: var(--white);
  }
  .screen { position: relative; width: 675px; height: 1200px; overflow: hidden; background: var(--bg-deep); }

  .hero-photo {
    position: absolute; left: 0; top: 0; width: 675px; height: 860px;
    background:
      radial-gradient(ellipse 260px 140px at 120px 640px, rgba(22,33,44,0.75), transparent 75%),
      radial-gradient(ellipse 140px 170px at 210px 580px, rgba(22,33,44,0.7), transparent 75%),
      radial-gradient(ellipse 340px 200px at 420px 520px, rgba(142,166,189,0.55), transparent 72%),
      radial-gradient(ellipse 380px 150px at 300px 260px, rgba(95,124,152,0.6), transparent 75%),
      radial-gradient(ellipse 200px 260px at 60px 360px, rgba(142,166,189,0.45), transparent 75%),
      radial-gradient(ellipse 200px 120px at 600px 460px, rgba(22,33,44,0.55), transparent 75%),
      linear-gradient(180deg, var(--hero-top) 0%, var(--hero-mid) 30%, var(--bg-mid) 70%, var(--bg-deep) 100%);
  }

  .status-bar {
    position: absolute; left: 0; top: 0; width: 100%; height: 36px;
    display: flex; align-items: center; justify-content: space-between;
    padding: 0 12px; font-size: 22px; font-weight: 600;
  }
  .status-left, .status-right { display: flex; align-items: center; gap: 8px; width: 200px; }
  .status-right { justify-content: flex-end; }
  .status-time { font-weight: 700; }

  .brand {
    position: absolute; left: 0; top: 332px; width: 100%;
    text-align: center; font-size: 60px; line-height: 1; font-weight: 800;
    letter-spacing: 5px; text-transform: uppercase;
  }

  .auth-actions { position: absolute; left: 27px; top: 880px; width: 619px; }
  .auth-row { display: flex; justify-content: space-between; }
  .btn {
    display: flex; align-items: center; justify-content: center;
    height: 88px; font-size: 24px; letter-spacing: 1.5px; text-transform: uppercase;
    color: var(--white); text-decoration: none;
  }
  .btn-outline { width: 299px; border: 2px solid var(--line); }
  .btn-social { margin-top: 20px; width: 619px; height: 87px; background: var(--accent); border-radius: 3px; gap: 10px; }
  .btn-social strong { font-weight: 800; }

  .skip {
    position: absolute; left: 0; top: 1120px; width: 100%;
    display: flex; justify-content: center; align-items: center; gap: 10px;
    font-size: 22px; letter-spacing: 1.5px; color: var(--muted); text-decoration: none;
  }
</style>
</head>
<body>
<main class="screen">
  <div class="hero-photo" role="img" aria-label="Photo of a silver hatchback car parked in a showroom, shown in dark blue tones"></div>

  <div class="status-bar">
    <div class="status-left">
      <svg width="34" height="16" viewBox="0 0 34 16" aria-hidden="true">
        <rect x="0" y="11" width="5" height="5" fill="#fff"/>
        <rect x="8" y="8" width="5" height="8" fill="#fff"/>
        <rect x="16" y="4" width="5" height="12" fill="#fff"/>
        <rect x="24" y="0" width="5" height="16" fill="#fff"/>
      </svg>
      <span>Kestrel</span>
      <svg width="26" height="20" viewBox="0 0 26 20" aria-hidden="true">
        <path d="M13 19 L3 8 A14 14 0 0 1 23 8 Z" fill="#fff"/>
      </svg>
    </div>
    <span class="status-time">9:41 AM</span>
    <div class="status-right">
      <svg width="12" height="20" viewBox="0 0 12 20" aria-hidden="true">
        <path d="M1 5 L11 14 L6 19 L6 1 L11 6 L1 15" fill="none" stroke="#fff" stroke-width="2"/>
      </svg>
      <span>100%</span>
      <svg width="46" height="22" viewBox="0 0 46 22" aria-hidden="true">
        <rect x="1" y="1" width="40" height="20" rx="4" fill="none" stroke="#fff" stroke-width="2"/>
        <rect x="4" y="4" width="34" height="14" rx="2" fill="#fff"/>
        <rect x="42" y="7" width="3" height="8" rx="1" fill="#fff"/>
      </svg>
    </div>
  </div>

  <h1 class="brand">Motorplume</h1>

  <nav class="auth-actions">
    <div class="auth-row">
      <a class="btn btn-outline" href="#">Sign up</a>
      <a class="btn btn-outline" href="#">Sign in</a>
    </div>
    <a class="btn btn-social" href="#">Continue with <strong>Chatterloom</strong></a>
  </nav>

  <a class="skip" href="#">SKIP
    <svg width="12" height="18" viewBox="0 0 12 18" aria-hidden="true">
      <path d="M3 3 L9 9 L3 15" fill="none" stroke="#e4ebf2" stroke-width="2.2"/>
    </svg>
  </a>
</main>
</body>
</html>
```